New Plumbing Company

We are looking for a smart and creative business card design for our new plumbing company. We are looking for creativity and originality in our business cards.

Industry/Entity Type

Plumbing

Contact Information for Business Card

Crestline Plumbing
Peter Halvane
Managing Director
Telephone Number : 0481529604
Email : service@crestlineplumbing.com.au
Website : www.crestlineplumbing.com.au
Lic. 508264K

Colors
0692cd
33a6d7
000000

Requirements
Must have
• I want the business card to be designed on a black background using the blue tones i have selected as seen in the company logo.

```html
<!DOCTYPE html>
<html lang="en">
<head>
<meta charset="utf-8">
<title>Crestline Plumbing — Business Card</title>
<link href="https://fonts.googleapis.com/css2?family=Jost:wght@400;500&display=swap" rel="stylesheet">
<style>
  :root {
    --page-bg: #8c8c8c;
    --card-black: #060505;
    --card-blue: #1169a8;
    --brand-blue: #0692cd;
    --brand-blue-light: #33a6d7;
    --text-light: #d9d9d9;
    --text-dark: #0a0a0a;
  }
  * { margin: 0; padding: 0; box-sizing: border-box; }
  html, body {
    width: 1105px;
    height: 1200px;
    overflow: hidden;
    background: var(--page-bg);
    font-family: "Jost", sans-serif;
  }
  .card {
    position: absolute;
    left: 182px;
    width: 746px;
    height: 425px;
  }
  .card-front { top: 119px; background: var(--card-black); }
  .card-back { top: 637px; background: var(--card-blue); }

  .brand {
    position: absolute;
    display: flex;
    align-items: center;
    gap: 16px;
  }
  .brand-mark {
    width: 62px;
    height: 62px;
    border-radius: 50%;
    border: 5px solid var(--brand-blue);
    flex: none;
  }
  .brand-name {
    font-weight: 400;
    font-size: 42px;
    line-height: 1;
    color: var(--brand-blue);
    white-space: nowrap;
  }
  .card-front .brand { left: 42px; top: 131px; }

  .person {
    position: absolute;
    left: 43px;
    top: 262px;
  }
  .person-name {
    font-weight: 500;
    font-size: 28px;
    letter-spacing: 0.5px;
    color: var(--brand-blue);
    text-transform: uppercase;
    line-height: 1.2;
  }
  .person-title {
    font-size: 20px;
    color: var(--text-light);
    line-height: 1.3;
  }

  .contact {
    position: absolute;
    left: 313px;
    top: 264px;
    list-style: none;
    font-size: 19px;
    line-height: 30px;
    color: var(--text-light);
  }

  .card-back .brand {
    left: 50%;
    top: 150px;
    transform: translateX(-50%);
  }
  .card-back .brand-mark { border-color: var(--text-dark); }
  .card-back .brand-name { color: var(--text-dark); }
  .back-web {
    position: absolute;
    left: 0;
    right: 0;
    top: 358px;
    text-align: center;
    font-size: 19px;
    letter-spacing: 2px;
    color: var(--text-dark);
  }
</style>
</head>
<body>
  <section class="card card-front">
    <div class="brand">
      <span class="brand-mark"></span>
      <span class="brand-name">Crestline Plumbing</span>
    </div>
    <div class="person">
      <p class="person-name">Peter Halvane</p>
      <p class="person-title">Managing Director</p>
    </div>
    <ul class="contact">
      <li>Lic. 508264K</li>
      <li>P : 0481529604</li>
      <li>service@crestlineplumbing.com.au</li>
      <li>www.crestlineplumbing.com.au</li>
    </ul>
  </section>

  <section class="card card-back">
    <div class="brand">
      <span class="brand-mark"></span>
      <span class="brand-name">Crestline Plumbing</span>
    </div>
    <p class="back-web">www.crestlineplumbing.com.au</p>
  </section>
</body>
</html>
```